Web Site Upgrade. Word Press Design.

Brimholt Pty Ltd
www.brimholt-example.com.au
Australia
Please see below design requirements for re-branding and renaming the Brimholt Pty. Ltd. To the new site to “Vornley Seating Co” Chairs + Bar Stools + More:
url: www.vornleyseating-example.com.au Already registered and hosting in place.
• Incorporate new logo in to site. (supplied in various formats including Adobe Illustrator)
• This will need to be Brimholt trading as (T/A) “Vornley Seating Co” Chairs + Bar Stools + More. Using Brimholt ABN as shown on current site.
• Redesign template to reflect new colour scheme. To be decided
• Provide a maximum of three PDF concepts for a new design and a minimum of two.
• Redesign home page text, graphics, photos Etc. To make it more appealing to visitors. Points to remember here are:
• Our market is Cafe and Restaurant owners. Not the general public.
• Brimholt tables are our own design for which we won the NBQ’s Fresh Tinkerers.
• Existing site is done in Word Press.
• Web hosting has already been orgainsed with Quarrow Hosting so it will be a case of uploading new site to existing host.
• Create a redirect to new site from old Brimholt Site.
• Check all pages check for any SEO issues.
Other than the changes made to the home page template which will be reflected in the rest of the pages, the rest of the site will remain unchanged for the time being.
NEW LOGO DESIGN
Target Market(s)
Cafe and Restaurant owners
Industry/Entity Type
Cafe
Requirements
Must have
- Incorporate images of products sold on web site.
Maintain functionality of existing site
Not 100% committed to new logo. Happy to see other suggestions.
Nice to have
- Really friendly SEO properties.
Design to make people go further than the home page and stay on the site
Should not have
- Too cluttered a look.

```html
<!DOCTYPE html>
<html lang="en">
<head>
<meta charset="utf-8">
<title>Vornley Seating Co – Chairs + Bar Stools + More</title>
<link href="https://fonts.googleapis.com/css2?family=Open+Sans:ital,wght@0,300;0,400;0,600;1,400&display=swap" rel="stylesheet">
<style>
:root{
  --orange:#ee5a35;
  --orange-light:#f57b52;
  --orange-dark:#e24a27;
  --red-head:#e8492a;
  --ink:#222;
  --body:#555;
  --muted:#777;
  --line:#e2e2e2;
  --footer-bg:#f4f4f4;
  --white:#fff;
}
*{box-sizing:border-box;margin:0;padding:0}
html,body{width:876px;height:1200px;overflow:hidden;background:var(--white)}
body{font-family:"Open Sans",Arial,sans-serif;color:var(--body);position:relative}
.abs{position:absolute}
.lines{white-space:nowrap}

/* header */
.brand{left:86px;top:20px;display:flex;align-items:center;gap:10px}
.brand-mark{width:22px;height:22px;background:var(--ink)}
.brand-name{font-size:19px;font-weight:600;color:var(--ink);line-height:1.1}
.brand-tag{left:118px;top:52px;font-size:10px;color:var(--ink)}
.order{right:94px;top:42px;text-align:right}
.order-label{font-size:11px;color:var(--ink);letter-spacing:.3px}
.order-phone{font-size:18px;color:var(--ink);line-height:1.1}
.order-abn{font-size:11.5px;color:var(--orange);margin-top:4px}
.social{left:584px;top:71px;display:flex;gap:7px}
.social span{width:17px;height:17px;border-radius:2px;background:#3b6fb6}
.social span:nth-child(2){background:#4fb3e8}
.social span:nth-child(3){background:#1f7ab8}

/* nav */
.nav{left:0;top:101px;width:876px;height:41px;background:linear-gradient(var(--orange-light),var(--orange-dark));display:flex;justify-content:center}
.nav a{color:var(--white);text-decoration:none;font-size:12px;line-height:41px;padding:0 13px;border-left:1px solid rgba(0,0,0,.12)}
.nav a:first-child{border-left:none}

/* hero */
.hero-title{left:86px;top:226px;font-size:25px;font-weight:600;color:var(--orange)}
.hero-sub{left:86px;top:261px;font-size:16.5px;font-weight:600;color:var(--ink)}
.hero-text{left:87px;top:290px;font-size:10px;line-height:17px;color:var(--muted)}
.hero-dots{left:86px;top:334px;display:flex;gap:3px}
.hero-dots span{width:10px;height:10px;border-radius:50%;background:#444}
.hero-photo{left:456px;top:152px;width:344px;height:282px;background:radial-gradient(ellipse at 55% 45%,#e23a33 0%,#d8d8d8 45%,#fafafa 75%)}
.hero-rule{left:0;top:434px;width:876px;height:1px;background:var(--line)}

/* products */
.products{left:78px;top:444px;width:717px;height:186px;display:flex;border:1px solid var(--line)}
.card{flex:1;border-left:1px solid var(--line);padding:12px 0 0 18px;background:linear-gradient(#fff,#fafafa)}
.card:first-child{border-left:none}
.card-img{width:100px;height:96px;margin-left:18px;border-radius:6px}
.card-name{font-size:12.5px;color:var(--ink);margin-top:14px}
.card-desc{font-size:9.5px;line-height:14.5px;color:var(--muted);margin-top:2px}
.arrow{top:508px}

/* content */
.h-light{font-size:21px;font-weight:300;color:var(--ink)}
.h-red{font-size:21px;font-weight:300;color:var(--red-head)}
.welcome{left:83px;top:659px}
.welcome .lead{font-size:11px;line-height:16px;color:#444;margin:12px 0 7px 2px}
.welcome p{font-size:9.2px;line-height:15.5px;margin:0 0 7px 2px}
.video-title{left:514px;top:656px}
.video{left:516px;top:688px;width:272px;height:166px;border:1px solid var(--line);box-shadow:0 1px 3px rgba(0,0,0,.1);padding:6px}
.video-still{width:100%;height:100%;background:linear-gradient(160deg,#8a6a55,#6e6f73 55%,#9a9ca0)}
.play{left:635px;top:754px}

.say-title{left:81px;top:884px}
.say-photo{left:83px;top:922px;width:140px;height:116px;background:linear-gradient(135deg,#6a7f73,#3e4a52 60%,#8b8f93)}
.say-quote{left:237px;top:920px;font-size:9px;font-style:italic;line-height:16.7px;color:#444}
.say-author{left:237px;top:1024px;font-size:11.5px;color:var(--ink)}
.reviews-title{left:517px;top:886px}
.review{left:518px;font-size:8.5px;font-style:italic;line-height:14px;color:var(--muted)}
.review-name{left:518px;font-size:9.5px;color:var(--ink)}

/* footer */
.footer{left:0;top:1100px;width:876px;height:100px;background:var(--footer-bg);border-top:1px solid var(--line)}
.foot-nav{left:85px;top:1124px;font-size:10px;color:var(--ink)}
.foot-nav span{margin:0 5px}
.copy{left:85px;top:1146px;font-size:9.5px;color:#666}
.pay{left:644px;top:1123px;display:flex;gap:4px}
.pay span{width:29px;height:19px;border:1px solid #bbb;background:#fff}
.pay span:last-child{width:50px}
</style>
</head>
<body>

<header>
  <div class="abs brand"><span class="brand-mark"></span><span class="brand-name">Vornley Seating Co</span></div>
  <div class="abs brand-tag">Chairs + Bar Stools + More</div>
  <div class="abs social" aria-label="Social links"><span></span><span></span><span></span></div>
  <div class="abs order">
    <div class="order-label">ORDER NOW</div>
    <div class="order-phone">0400 123 456</div>
    <div class="order-abn">ABN 00 000 000 000</div>
  </div>
</header>

<nav class="abs nav">
  <a>HOME</a><a>ABOUT</a><a>CAFE TABLES</a><a>TABLE BASES</a><a>TABLE TOPS</a><a>CAFE CHAIRS</a><a>BAR STOOLS</a><a>BLOG</a><a>CONTACT</a>
</nav>

<section class="hero">
  <h1 class="abs hero-title">DONEC DICTUM LECTUS NON</h1>
  <h2 class="abs hero-sub">MAURIS NUNC QUAM VENENATIS NEC</h2>
  <p class="abs hero-text lines">Sit amet egestas placerat est Pellentesque habitant morbi tris-<br>tique senectus et netus et malesuada Praesent elem</p>
  <div class="abs hero-dots"><span></span><span></span><span></span><span></span></div>
  <div class="abs hero-photo" role="img" aria-label="Square white cafe table with four red armchairs"></div>
  <div class="abs hero-rule"></div>
</section>

<section class="abs products">
  <div class="card"><div class="card-img" role="img" aria-label="Green cafe chair" style="background:radial-gradient(circle,#8ccf4a 0%,#f4f4f4 70%)"></div><div class="card-name">Product Name</div><div class="card-desc">Etiam eu urna Sed porta Suspend-<br>isse quam leo molestie sed</div></div>
  <div class="card"><div class="card-img" role="img" aria-label="Round white table with cross base" style="background:radial-gradient(circle,#dcdcdc 0%,#f7f7f7 70%)"></div><div class="card-name">Product Name</div><div class="card-desc">Etiam eu urna Sed porta Suspend-<br>isse quam leo molestie sed</div></div>
  <div class="card"><div class="card-img" role="img" aria-label="Square and round table tops" style="background:radial-gradient(circle,#e6d9d4 0%,#f7f7f7 70%)"></div><div class="card-name">Product Name</div><div class="card-desc">Etiam eu urna Sed porta Suspend-<br>isse quam leo molestie sed</div></div>
  <div class="card"><div class="card-img" role="img" aria-label="Black cafe armchair" style="background:radial-gradient(circle,#3a3d42 0%,#f4f4f4 70%)"></div><div class="card-name">Product Name</div><div class="card-desc">Etiam eu urna Sed porta Suspend-<br>isse quam leo molestie sed</div></div>
</section>
<svg class="abs arrow" style="left:46px" width="22" height="50" viewBox="0 0 22 50"><path d="M20 2 L2 25 L20 48" fill="none" stroke="#ccc" stroke-width="1.3"/></svg>
<svg class="abs arrow" style="left:803px" width="22" height="50" viewBox="0 0 22 50"><path d="M2 2 L20 25 L2 48" fill="none" stroke="#ccc" stroke-width="1.3"/></svg>

<section class="abs welcome lines">
  <h2 class="h-light">Welcome to Our Website Mainpage</h2>
  <p class="lead">Aliquam nec erat at purus cursus interdum Vestibulum ligula augue biben-<br>dum accumsan vestibulum ut commodo a mi Morbi ornare</p>
  <p>Maecenas at justo id velit placerat molestie Donec dictum lectus non odio Cras a ante<br>vitae enim iaculis aliquam Mauris nunc quam venenatis nec euismod sit amet egestas<br>placerat est Pellentesque habitant morbi tristique senectus et netus et malesuada</p>
  <p>Aliquam nec erat at purus cursus interdum Vestibulum ligula augue bibendum accum-<br>san vestibulum ut commodo a mi Morbi ornare gravida elit Integer congue augue et<br>malesuada iaculis ipsum dui aliquet felis at cursus</p>
</section>

<h2 class="abs h-red video-title">Watch Our Video</h2>
<div class="abs video"><div class="video-still" role="img" aria-label="Video still of a Brimholt adjustable table foot on decking"></div></div>
<svg class="abs play" width="34" height="34" viewBox="0 0 34 34"><circle cx="17" cy="17" r="15" fill="rgba(255,255,255,.85)" stroke="#222" stroke-width="2.5"/><path d="M14 11 L23 17 L14 23 Z" fill="#222"/></svg>

<h2 class="abs h-light say-title">What Our Customer Say</h2>
<div class="abs say-photo" role="img" aria-label="Cafe interior with clear acrylic chairs"></div>
<p class="abs say-quote lines">Mauris nunc quam venenatis nec euismod sit amet ege-<br>stas placerat est Pellentesque habitant morbi tristique<br>senectus et netus et malesuada fames ac turpis egestas<br>Cras id elit Integer quis urna Ut ante enim dapibus<br>malesuada fringilla eu condimentum quis tellus Aenean<br>porttitor eros vel dolor Donec convallis pede</p>
<div class="abs say-author">By Author Name</div>

<h2 class="abs h-red reviews-title">Latest Reviews</h2>
<p class="abs review lines" style="top:919px">Aliquam nec erat at purus cursus interdum Vestibulum ligula augue<br>bibendum accumsan vestibulum ut commodo a mi Morbi ornare gravida<br>elit Integer congue augue et malesuada iaculis ipsum dui aliquet</p>
<div class="abs review-name" style="top:964px">- Person Name</div>
<p class="abs review lines" style="top:987px;left:520px">Aliquam nec erat at purus cursus interdum Vestibulum ligula augue<br>bibendum accumsan vestibulum ut commodo a mi Morbi ornare gravida<br>elit Integer congue augue et malesuada iaculis ipsum dui</p>
<div class="abs review-name" style="top:1030px">- Person Name</div>

<footer class="abs footer"></footer>
<div class="abs foot-nav">HOME<span>|</span>ABOUT<span>|</span>CAFE TABLES<span>|</span>TABLE BASES<span>|</span>TABLE TOPS<span>|</span>CAFE CHAIRS<span>|</span>BLOG<span>|</span>CONTACT</div>
<div class="abs copy">© 2014 Company Name &nbsp;All right reserved &nbsp;Term of Use</div>
<div class="abs pay" aria-label="Accepted payment methods"><span></span><span></span><span></span><span></span></div>

</body>
</html>
```